Business Cards for Marco and Tobin

Design of business cards for two people with the recently created brand Valcor Mobile. Valcor Mobile wants to become a worldwide major player on the secondhand phone market. It gathers send hand phones from individuals, refurbish them and sell them throughout the world. It has a green impact (recycling) and we also contribute to social project in Africa (a percentage of our benefits are sent to build school, sport facilities, etc.

Target Market(s)

B2B - Marco and Tobin are in contact with distributors across Africa.

Industry/Entity Type

Wireless Communication

Contact Information for Business Card

Marco Feuillet
Head of Emerging Markets
Valcor Energy South Africa (Pty) Ltd
Kestrel Road 47
2031 Sandton - Johannesburg
South Africa
Tel: + 27 10 555 0148
Mobile : +27 82 55 104
Email : marco.feuillet@valcormobile.example
Skype: marco.feuillet
Web: www.valcormobile.example
 

Tobin Farrow
Head of Southern Africa
Kestrel Road 47
South Africa
Tel: + 27 10 555 0148
Mobile: +27 83 555 0276
Email: tobin.farrow@valcormobile.example
Skype: tobin.farrow
Web: www.valcormobile.example

Requirements
Must have
• The cards need to be "serious", trustable, with a worldwide presence.
Nice to have
• Some "green" / recycling touch would be nice but not necessary if in contradiction with the general design.

```html
<!DOCTYPE html>
<html lang="en">
<head>
<meta charset="utf-8">
<title>Valcor Mobile Business Card</title>
<link rel="stylesheet" href="https://fonts.googleapis.com/css2?family=Open+Sans:wght@400;600;700&display=swap">
<style>
  :root {
    --backdrop: #2b2b2d;
    --navy: #263850;
    --brand-blue: #3592d5;
    --ink: #1b1d22;
    --paper: #ffffff;
    --muted: #d5dbe4;
    --eco-green: #3cb233;
  }
  * { box-sizing: border-box; margin: 0; padding: 0; }
  html, body { width: 1200px; height: 900px; overflow: hidden; }
  body {
    background: var(--backdrop);
    font-family: "Open Sans", Arial, sans-serif;
    position: relative;
  }
  .card {
    position: absolute;
    left: 230px;
    width: 740px;
    height: 420px;
    overflow: hidden;
    box-shadow: 0 10px 28px rgba(0,0,0,.55);
  }
  .card--back { top: 22px; background: var(--navy); }
  .card--front { top: 460px; background: var(--paper); }

  .brand {
    display: flex;
    align-items: center;
    gap: 14px;
    font-weight: 700;
    letter-spacing: -0.5px;
  }
  .brand__square { width: 30px; height: 30px; background: var(--brand-blue); }

  .card--back .brand {
    position: absolute; top: 150px; left: 0; right: 0;
    justify-content: center;
    color: var(--paper);
    font-size: 50px;
  }
  .card--back .back-line {
    position: absolute; top: 262px; left: 0; right: 0;
    text-align: center;
    color: var(--muted);
    font-size: 17px;
    letter-spacing: 2px;
  }

  .front-art { position: absolute; inset: 0; }
  .card--front .brand {
    position: absolute; top: 62px; left: 48px;
    color: var(--navy);
    font-size: 46px;
  }
  .contacts {
    position: absolute; top: 190px; left: 48px;
    list-style: none;
    font-size: 19px;
    color: var(--ink);
    line-height: 30px;
  }
  .contacts li { display: flex; align-items: center; gap: 14px; }
  .contacts svg { width: 20px; height: 20px; flex: none; }

  .person {
    position: absolute; right: 36px; top: 222px;
    text-align: right;
    color: var(--ink);
    font-size: 17px;
    line-height: 25px;
  }
  .person__name { color: var(--brand-blue); font-weight: 700; font-size: 26px; line-height: 34px; }
  .person__role { margin-bottom: 10px; }
</style>
</head>
<body>

<section class="card card--back">
  <div class="brand"><span class="brand__square"></span>Valcor Mobile</div>
  <p class="back-line">marco.feuillet www.valcormobile.example</p>
</section>

<section class="card card--front">
  <svg class="front-art" viewBox="0 0 740 420" width="740" height="420" aria-hidden="true">
    <path d="M280,0 C500,28 690,150 740,320 L740,0 Z" fill="#3592d5"/>
    <path d="M315,0 C515,26 675,132 740,262 L740,0 Z" fill="#ffffff"/>
    <path d="M330,0 C520,24 675,122 740,250 L740,0 Z" fill="#263850"/>
    <circle cx="662" cy="84" r="28" fill="#3cb233" role="img" aria-label="Recycling symbol"/>
  </svg>

  <div class="brand"><span class="brand__square"></span>Valcor Mobile</div>

  <ul class="contacts">
    <li>
      <svg viewBox="0 0 24 24"><path fill="#3592d5" d="M6.6 10.8a15 15 0 0 0 6.6 6.6l2.2-2.2a1 1 0 0 1 1-.25 11.4 11.4 0 0 0 3.6.6 1 1 0 0 1 1 1V20a1 1 0 0 1-1 1A17 17 0 0 1 3 4a1 1 0 0 1 1-1h3.5a1 1 0 0 1 1 1c0 1.25.2 2.45.6 3.6a1 1 0 0 1-.25 1z"/></svg>
      +27 10 555 0148
    </li>
    <li>
      <svg viewBox="0 0 24 24"><path fill="#3592d5" d="M6 3h12v5H6zM4 9h16a2 2 0 0 1 2 2v6h-4v4H6v-4H2v-6a2 2 0 0 1 2-2zm4 6v4h8v-4z"/></svg>
      +27 82 55 104
    </li>
    <li>
      <svg viewBox="0 0 24 24"><circle cx="12" cy="12" r="10" fill="#3592d5"/></svg>
      marco.feuillet
    </li>
    <li>
      <svg viewBox="0 0 24 24"><path fill="#3592d5" d="M2 5h20v14H2zm2 2v.5l8 5.5 8-5.5V7z"/></svg>
      marco.feuillet@valcormobile.example
    </li>
    <li>
      <svg viewBox="0 0 24 24" fill="none" stroke="#3592d5" stroke-width="2"><circle cx="12" cy="12" r="9"/><path d="M3 12h18M12 3c3 3 3 15 0 18M12 3c-3 3-3 15 0 18"/></svg>
      marco.feuillet www.valcormobile.example
    </li>
  </ul>

  <div class="person">
    <p class="person__name">Marco Feuillet</p>
    <p class="person__role">Head of Emerging Markets</p>
    <p>Valcor Energy South Africa (Pty) Ltd</p>
    <p>Kestrel Road 47</p>
    <p>2031 Sandton - Johannesburg</p>
    <p>South Africa</p>
  </div>
</section>

</body>
</html>
```